quarry-mosaic artisans and studio

I need a web design for my company we offer counter tops. tile for floors,showers,kitchen backsplashes and more also need a place where the client
can write reviews

```html
<!DOCTYPE html>
<html lang="en">
<head>
<meta charset="utf-8">
<title>Quarry-Mosaic Artisans — Tile &amp; Countertops</title>
<link rel="stylesheet" href="https://fonts.googleapis.com/css2?family=Arimo:wght@400;700&family=Roboto+Condensed:wght@700&display=swap">
<style>
  :root {
    --page-bg: #f6f6f5;
    --ink: #1f1f1f;
    --ink-soft: #2b2b2b;
    --accent: #2a8db5;
    --footer-bg: #238cb4;
    --footer-ink: #ffffff;
    --rule: #6d6d6d;
    --veil: rgba(255, 255, 255, 0.55);
  }
  * { box-sizing: border-box; margin: 0; padding: 0; }
  html, body { width: 691px; height: 1200px; overflow: hidden; }
  body {
    position: relative;
    background: var(--page-bg);
    font-family: "Arimo", Arial, sans-serif;
    color: var(--ink);
  }
  .abs { position: absolute; }

  /* Top navigation */
  .main-nav { left: 22px; top: 18px; display: flex; gap: 14px; font-size: 13.5px; letter-spacing: 0.4px; }
  .main-nav a { color: var(--ink); text-decoration: none; }
  .main-nav a.is-current { color: var(--accent); text-decoration: underline; }
  .search-label { left: 560px; top: 17px; font-size: 8.5px; letter-spacing: 0.6px; }
  .search-box { left: 558px; top: 31px; width: 113px; height: 19px; border: 1px solid #333; background: #fff; }
  .search-box svg { position: absolute; right: 4px; top: 2px; }

  /* Brand header */
  .brand-name {
    left: 0; width: 691px; top: 78px; text-align: center;
    font-family: "Roboto Condensed", "Arial Narrow", sans-serif; font-weight: 700;
    font-size: 40px; color: var(--ink-soft); letter-spacing: 0.5px;
  }
  .brand-tagline {
    left: 0; width: 691px; top: 127px; text-align: center;
    font-size: 18.5px; letter-spacing: 4.6px; color: var(--accent);
  }

  /* Hero */
  .hero-image {
    left: 0; top: 182px; width: 691px; height: 411px;
    background: linear-gradient(180deg, #e9ecec 0%, #f4f5f4 45%, #dfe1df 70%, #9c7f66 100%);
  }
  .hero-veil {
    left: 36px; top: 244px; width: 564px; height: 200px;
    background: var(--veil); border-radius: 0 40px 0 40px;
  }
  .hero-headline {
    font-family: "Roboto Condensed", "Arial Narrow", sans-serif; font-weight: 700;
    font-size: 42px; line-height: 44px; color: var(--ink-soft);
  }
  .hero-line-1 { left: 63px; top: 276px; }
  .hero-line-2 { right: 139px; top: 320px; }
  .hero-sub {
    right: 147px; top: 376px; text-align: center;
    font-size: 20px; line-height: 20px; color: var(--accent);
  }
  .hero-button {
    left: 542px; top: 524px; width: 149px; height: 44px;
    background: rgba(255,255,255,0.8); border-radius: 22px 0 0 22px;
    font-family: "Roboto Condensed", "Arial Narrow", sans-serif; font-weight: 700;
    font-size: 19px; line-height: 44px; padding-left: 20px; color: var(--ink-soft);
  }

  /* New products */
  .section-title {
    left: 0; width: 691px; top: 636px; text-align: center;
    font-family: "Roboto Condensed", "Arial Narrow", sans-serif; font-weight: 700;
    font-size: 31px; letter-spacing: 1.5px; color: var(--accent);
  }
  .section-rule { left: 114px; top: 678px; width: 460px; height: 2px; background: var(--rule); }

  .product-card { top: 714px; width: 145px; }
  .product-swatch { width: 145px; height: 144px; box-shadow: 1px 2px 4px rgba(0,0,0,0.35); }
  .product-name { margin-top: 14px; text-align: center; font-size: 18px; }
  .product-price { margin-top: 4px; padding-left: 10px; font-size: 14.5px; line-height: 22px; }
  .product-price .price { color: var(--accent); }
  .product-more { text-align: right; padding-right: 4px; margin-top: 2px; font-size: 11px; color: #1d5f86; }

  .swatch-black { background: radial-gradient(circle at 40% 40%, #2e2f2f, #151616); }
  .swatch-sand { background: radial-gradient(circle at 50% 50%, #d7bb98, #b8926d); }
  .swatch-granite { background: linear-gradient(135deg, #cfa88a 0%, #e6d3c3 45%, #a9826a 100%); }
  .swatch-grey { background: radial-gradient(circle at 50% 50%, #6a6b6d, #3d3e40); }

  /* Footer */
  .site-footer {
    left: 0; top: 1024px; width: 691px; height: 176px;
    background: var(--footer-bg); color: var(--footer-ink);
    font-size: 13.5px; letter-spacing: 0.5px;
  }
  .footer-contact { left: 22px; top: 22px; line-height: 18.5px; }
  .footer-contact strong { display: block; margin-top: 3px; }
  .footer-links { left: 382px; top: 22px; line-height: 16.5px; }
  .footer-copyright {
    right: 20px; bottom: 14px;
    font-family: "Roboto Condensed", "Arial Narrow", sans-serif; font-weight: 700; font-size: 12.5px;
    display: flex; align-items: center; gap: 3px;
  }
</style>
</head>
<body>
  <nav class="main-nav abs">
    <a href="#" class="is-current">HOME</a>
    <a href="#">PRODUCTS</a>
    <a href="#">CONTACT US</a>
    <a href="#">REVIEWS</a>
  </nav>
  <div class="search-label abs">Search Our Products</div>
  <div class="search-box abs">
    <svg width="14" height="14" viewBox="0 0 14 14" aria-hidden="true">
      <circle cx="8.5" cy="5.5" r="3.8" fill="none" stroke="#111" stroke-width="1.6"/>
      <line x1="5.7" y1="8.3" x2="1.5" y2="12.5" stroke="#111" stroke-width="2"/>
    </svg>
  </div>

  <h1 class="brand-name abs">QUARRY-MOSAIC ARTISANS</h1>
  <p class="brand-tagline abs">Specializing in tile &amp; countertops</p>

  <div class="hero-image abs" role="img" aria-label="Bright white kitchen with marble island, upholstered stools and pendant lights"></div>
  <div class="hero-veil abs"></div>
  <div class="hero-headline hero-line-1 abs">Check out our newest</div>
  <div class="hero-headline hero-line-2 abs">selection of tile!</div>
  <p class="hero-sub abs">Call now for a custom<br>quote on your next project!</p>
  <a class="hero-button abs">Learn More...</a>

  <h2 class="section-title abs">New Products</h2>
  <div class="section-rule abs"></div>

  <div class="product-card abs" style="left:19px">
    <div class="product-swatch swatch-black" role="img" aria-label="Black speckled countertop sample"></div>
    <div class="product-name">Countertop</div>
    <div class="product-price">Starting at <span class="price">2.99</span><br>per sq. inch</div>
    <div class="product-more">View More...</div>
  </div>
  <div class="product-card abs" style="left:187px">
    <div class="product-swatch swatch-sand" role="img" aria-label="Sand-coloured quartz countertop sample"></div>
    <div class="product-name">Countertop</div>
    <div class="product-price">Starting at <span class="price">2.99</span><br>per sq. inch</div>
    <div class="product-more">View More...</div>
  </div>
  <div class="product-card abs" style="left:356px">
    <div class="product-swatch swatch-granite" role="img" aria-label="Pink and beige granite countertop sample"></div>
    <div class="product-name">Countertop</div>
    <div class="product-price">Starting at <span class="price">2.99</span><br>per sq. inch</div>
    <div class="product-more">View More...</div>
  </div>
  <div class="product-card abs" style="left:524px">
    <div class="product-swatch swatch-grey" role="img" aria-label="Grey speckled countertop sample"></div>
    <div class="product-name">Countertop</div>
    <div class="product-price">Starting at <span class="price">2.99</span><br>per sq. inch</div>
    <div class="product-more">View More...</div>
  </div>

  <footer class="site-footer abs">
    <div class="footer-contact abs">
      Installation questions: 000-000-000<br>
      Product questions: 000-000-000
      <strong>Hours of Operation</strong>
      Monday - Friday: 8:00 a.m. - 9:00 p.m.<br>
      Saturday: 8:00 a.m. - 6:00 p.m.<br>
      Sunday: Closed
    </div>
    <div class="footer-links abs">
      <strong>Company Info</strong><br>
      Contact Us<br>
      FAQ'S<br>
      Terms and Conditions
    </div>
    <div class="footer-copyright abs">
      <svg width="12" height="12" viewBox="0 0 12 12" aria-hidden="true"><circle cx="6" cy="6" r="5.2" fill="none" stroke="#fff" stroke-width="1"/><path d="M7.8 4.5A2.3 2.3 0 1 0 7.8 7.5" fill="none" stroke="#fff" stroke-width="1"/></svg>
      Quarry-Mosaic Artisans 2014
    </div>
  </footer>
</body>
</html>
```